Need a design package for hair towels wrap

We need package design for hair towel wrap ( 3 pack) brand name is The Vostra. We are looking for simple, contemporary and unique design, color palette 2-3 colors. Paper Box size is 9*8*3 inches with PVC window.Actual picture of the product won't be on the package.Attached Brand Logo and description for the package. Barcode needed to be included on the design package.It will be provided later. Attached sample of the box from manufacturer, and instruction for towel wrap which idea I like, if you could make something similar to it, would be great.

Target Market(s)

Kestrel

Industry/Entity Type

Hair

Colors
848484
f5f5f5
faa54b
333333

Requirements
Must have
• Clean, contemporary design.

```html
<!DOCTYPE html>
<html lang="en">
<head>
<meta charset="UTF-8">
<title>The Vostra – Microfiber Hair Towel Wrap Box</title>
<link href="https://fonts.googleapis.com/css2?family=Open+Sans:wght@300;400;600;700&display=swap" rel="stylesheet">
<style>
  :root {
    --page-bg: #e9e9e9;
    --charcoal: #2a2a2a;
    --charcoal-soft: #333333;
    --amber: #d6984f;
    --gold: #c9993f;
    --white: #f5f5f5;
    --grey-text: #9a9a9a;
    --towel-light: #e6e6e2;
    --towel-shade: #c9c9c4;
  }
  * { box-sizing: border-box; margin: 0; padding: 0; }
  html, body {
    width: 1200px; height: 900px; overflow: hidden;
    background: var(--page-bg);
    font-family: "Open Sans", Arial, sans-serif;
  }
  .dieline {
    position: absolute; left: 120px; top: 130px;
    display: flex; height: 640px;
    box-shadow: 0 18px 40px rgba(0,0,0,.18);
  }
  /* Side panel */
  .side-panel {
    width: 240px; height: 100%;
    background: var(--charcoal-soft);
    padding: 40px 26px 30px 26px;
    display: flex; flex-direction: column; justify-content: space-between;
    border-right: 1px solid #1e1e1e;
  }
  .feature-list { list-style: none; }
  .feature-list li {
    position: relative; padding-left: 22px; margin-bottom: 24px;
    color: var(--grey-text); font-size: 14px; line-height: 1.45;
  }
  .feature-list li::before {
    content: ""; position: absolute; left: 0; top: 5px;
    width: 9px; height: 9px; background: var(--amber);
  }
  .care-info { color: var(--grey-text); font-size: 12px; line-height: 1.5; }
  .care-icons { display: flex; gap: 8px; margin: 8px 0; }
  .care-icons span {
    width: 20px; height: 20px; border: 1.5px solid var(--grey-text); border-radius: 3px;
  }
  /* Front panel */
  .front-panel {
    position: relative; width: 720px; height: 100%;
    background: linear-gradient(var(--charcoal) 0 55%, var(--amber) 55% 100%);
    text-align: center;
  }
  .brand-mark {
    position: absolute; left: 50%; top: 58px; transform: translateX(-50%);
    width: 52px; height: 52px; background: var(--gold);
  }
  .brand-name {
    position: absolute; top: 138px; width: 100%;
    color: var(--white); font-weight: 700; font-size: 34px; letter-spacing: 1px;
  }
  .product-title {
    position: absolute; top: 186px; width: 100%;
    color: var(--white); font-weight: 300; font-size: 42px; letter-spacing: 1px;
  }
  .product-window {
    position: absolute; left: 58px; top: 258px; width: 604px; height: 250px;
    border-radius: 14px; border: 3px solid rgba(245,245,245,.85);
    overflow: hidden;
  }
  .product-window svg { display: block; }
  .pack-count {
    position: absolute; top: 522px; width: 100%;
    color: var(--charcoal); font-weight: 700; font-size: 30px;
  }
  .tagline {
    position: absolute; top: 564px; width: 100%;
    color: var(--white); font-weight: 400; font-size: 25px; line-height: 1.3;
  }
</style>
</head>
<body>
  <div class="dieline">
    <aside class="side-panel">
      <ul class="feature-list">
        <li>Fits all head sizes.</li>
        <li>Suitable for all hair types and lengths. Helps in drying hair.</li>
        <li>Absorbs approximately 70% of the water within 10 mins.</li>
        <li>Less time blowdrying means healthier hair.</li>
        <li>Reduces risk of split ends, breakage and frizz.</li>
      </ul>
      <div class="care-info">
        <p>100% Microfiber, 3 Pieces</p>
        <div class="care-icons"><span></span><span></span><span></span><span></span></div>
        <p>Machine washable</p>
      </div>
    </aside>

    <section class="front-panel">
      <div class="brand-mark"></div>
      <h1 class="brand-name">THE VOSTRA</h1>
      <h2 class="product-title">MICROFIBER HAIR TOWEL WRAP</h2>
      <div class="product-window">
        <svg width="598" height="244" role="img" aria-label="Window showing three rolled light grey microfiber hair towels">
          <defs>
            <linearGradient id="towel" x1="0" x2="1">
              <stop offset="0" stop-color="var(--towel-shade)"/>
              <stop offset="0.5" stop-color="var(--towel-light)"/>
              <stop offset="1" stop-color="var(--towel-shade)"/>
            </linearGradient>
          </defs>
          <rect x="0" y="0" width="200" height="244" fill="url(#towel)"/>
          <rect x="200" y="0" width="200" height="244" fill="url(#towel)"/>
          <rect x="400" y="0" width="198" height="244" fill="url(#towel)"/>
        </svg>
      </div>
      <p class="pack-count">Set of 3 Hair Towels</p>
      <p class="tagline">The softest, ultra-absorbent, light &amp; safest<br>Towel for your beautiful hair.</p>
    </section>
  </div>
</body>
</html>
```